Harborline Wellness Partners

Please design a business card that is colorful but at the same time easy to read. We are based out on Miami Florida. We are a small start up healthcare company that has been in operation for 1 year. Our clients are Hospitals, Insurance companies, and Manage Care health companies. We are growing quickly and lead the niche we are in. Please make the card 2 sided on the front will be the typical info. Logo, Company Name, Persons Name, Title, Cell #, Office #, Fax#, email, website. No address. On the back we will list 5 services that we do. For example Care Transitions, Case management, Risk assessment, Utilization Review.
Target Market(s)
CEO's and COO's of hospitals and healthcare companies.
Industry/Entity Type
Healthcare

```html
<!DOCTYPE html>
<html lang="en">
<head>
<meta charset="utf-8">
<title>Harborline Wellness Partners – Business Card</title>
<link href="https://fonts.googleapis.com/css2?family=Open+Sans:wght@300;400;600;700&display=swap" rel="stylesheet">
<style>
  :root {
    --page: #e9e6e1;
    --card: #ffffff;
    --ink: #2b2b2b;
    --muted: #6b6b6b;
    --navy: #1f2f8f;
    --red: #e2343a;
    --yellow: #f4c21b;
    --green: #8cc63f;
    --blue: #1ea3e0;
    --faint: #ececec;
  }
  * { box-sizing: border-box; margin: 0; padding: 0; }
  html, body { width: 1200px; height: 809px; overflow: hidden; }
  body {
    background: var(--page);
    font-family: "Open Sans", Arial, sans-serif;
    color: var(--ink);
    position: relative;
  }
  .card {
    position: absolute;
    top: 250px;
    width: 540px;
    height: 310px;
    background: var(--card);
    box-shadow: 0 6px 18px rgba(0,0,0,0.12);
    overflow: hidden;
  }
  .card--back { left: 45px; }
  .card--front { left: 615px; }

  .stripe {
    position: absolute;
    top: 0;
    height: 100%;
    display: flex;
    flex-direction: column;
  }
  .stripe span { flex: 1; }
  .stripe .s-red { background: var(--red); }
  .stripe .s-yellow { background: var(--yellow); }
  .stripe .s-green { background: var(--green); }
  .stripe .s-blue { background: var(--blue); }
  .stripe--right { right: 0; width: 44px; }
  .stripe--left { left: 0; width: 14px; }

  /* Back side */
  .brand-mark {
    position: absolute;
    left: 40px;
    top: 70px;
    width: 190px;
    display: flex;
    align-items: center;
    gap: 12px;
  }
  .brand-dot {
    flex: none;
    width: 26px; height: 26px;
    border-radius: 50%;
    background: var(--blue);
  }
  .brand-name {
    font-weight: 700;
    font-size: 24px;
    line-height: 1.15;
    color: var(--navy);
  }
  .services {
    position: absolute;
    left: 260px;
    top: 78px;
    list-style: none;
  }
  .services li {
    display: flex;
    align-items: center;
    gap: 12px;
    font-size: 21px;
    font-weight: 300;
    line-height: 38px;
    color: var(--ink);
  }
  .services svg { width: 16px; height: 16px; }

  /* Front side */
  .front-brand {
    position: absolute;
    left: 44px;
    top: 36px;
    display: flex;
    align-items: center;
    gap: 12px;
  }
  .front-brand .brand-dot { width: 22px; height: 22px; }
  .front-brand .brand-name { font-size: 19px; width: 170px; }
  .faint-circle {
    position: absolute;
    right: 80px;
    top: 40px;
    width: 230px;
    height: 230px;
    border-radius: 50%;
    background: var(--faint);
  }
  .person {
    position: absolute;
    left: 190px;
    top: 130px;
  }
  .person-name {
    font-size: 21px;
    font-weight: 400;
    color: var(--ink);
  }
  .person-title {
    font-size: 9px;
    letter-spacing: 2px;
    text-transform: uppercase;
    color: var(--muted);
    margin-left: 40px;
  }
  .contacts {
    position: absolute;
    left: 44px;
    top: 180px;
    list-style: none;
  }
  .contacts li {
    display: flex;
    align-items: center;
    gap: 10px;
    font-size: 12.5px;
    line-height: 21px;
    color: var(--ink);
  }
  .contacts svg { width: 12px; height: 12px; fill: var(--ink); }
</style>
</head>
<body>

  <section class="card card--back" aria-label="Card back: services">
    <div class="brand-mark">
      <span class="brand-dot"></span>
      <span class="brand-name">Harborline Wellness Partners</span>
    </div>
    <ul class="services">
      <li><svg viewBox="0 0 16 16"><path d="M2 8 L6 13 L14 3" fill="none" stroke="#1ea3e0" stroke-width="2.6" stroke-linecap="round" stroke-linejoin="round"/></svg>Care Transitions</li>
      <li><svg viewBox="0 0 16 16"><path d="M2 8 L6 13 L14 3" fill="none" stroke="#8cc63f" stroke-width="2.6" stroke-linecap="round" stroke-linejoin="round"/></svg>Case management</li>
      <li><svg viewBox="0 0 16 16"><path d="M2 8 L6 13 L14 3" fill="none" stroke="#f4c21b" stroke-width="2.6" stroke-linecap="round" stroke-linejoin="round"/></svg>Risk assessment</li>
      <li><svg viewBox="0 0 16 16"><path d="M2 8 L6 13 L14 3" fill="none" stroke="#e2343a" stroke-width="2.6" stroke-linecap="round" stroke-linejoin="round"/></svg>Utilization Review</li>
    </ul>
    <div class="stripe stripe--right"><span class="s-red"></span><span class="s-yellow"></span><span class="s-green"></span><span class="s-blue"></span></div>
  </section>

  <section class="card card--front" aria-label="Card front: contact details">
    <div class="stripe stripe--left"><span class="s-red"></span><span class="s-yellow"></span><span class="s-green"></span><span class="s-blue"></span></div>
    <div class="faint-circle"></div>
    <div class="front-brand">
      <span class="brand-dot"></span>
      <span class="brand-name">Harborline Wellness Partners</span>
    </div>
    <div class="person">
      <p class="person-name">Marcus BELL</p>
      <p class="person-title">Manager</p>
    </div>
    <ul class="contacts">
      <li><svg viewBox="0 0 12 12"><rect x="3" y="0.5" width="6" height="11" rx="1" fill="none" stroke="#2b2b2b" stroke-width="1.2"/><circle cx="6" cy="9.5" r="0.8"/></svg>+00 00 0000 0000 000</li>
      <li><svg viewBox="0 0 12 12"><path d="M2.5 1 L4.5 1 L5.3 3.6 L4 4.6 Q5 7.2 7.4 8 L8.4 6.7 L11 7.5 L11 9.5 Q10.5 11 9 11 Q1 10 1 2.5 Q1 1 2.5 1 Z"/></svg>+00 00 0000 0000 000</li>
      <li><svg viewBox="0 0 12 12"><rect x="2" y="4" width="8" height="7" rx="1"/><rect x="3.5" y="1" width="5" height="3" fill="none" stroke="#2b2b2b"/></svg>+00 00 0000 0000 000</li>
      <li><svg viewBox="0 0 12 12"><rect x="0.5" y="2" width="11" height="8" fill="none" stroke="#2b2b2b" stroke-width="1.2"/><path d="M0.5 2 L6 7 L11.5 2" fill="none" stroke="#2b2b2b" stroke-width="1.2"/></svg>somewhere@somewhere.com</li>
      <li><svg viewBox="0 0 12 12"><circle cx="6" cy="6" r="5.2" fill="none" stroke="#2b2b2b" stroke-width="1.1"/><ellipse cx="6" cy="6" rx="2.2" ry="5.2" fill="none" stroke="#2b2b2b" stroke-width="0.9"/><path d="M1 6 H11" stroke="#2b2b2b" stroke-width="0.9"/></svg>www.somewhere.com</li>
    </ul>
    <div class="stripe stripe--right"><span class="s-red"></span><span class="s-yellow"></span><span class="s-green"></span><span class="s-blue"></span></div>
  </section>

</body>
</html>
```